Tovalmer's 50th Anniversary Gala

Need a cool invitation to be printed on #120 paper for a nonprofit gala fundraiser. Verbiage for invitation is below. Event logo is attached. Could potentially use black and gold but NOT a requirement. Want it to be FUN and DIFFERENT.

Colors
0054AA
0677BA
7BADD7
CADEEF
E8F1F8

```html
<!DOCTYPE html>
<html lang="en">
<head>
<meta charset="utf-8">
<title>Tovalmer's 50th Anniversary Gala</title>
<link href="https://fonts.googleapis.com/css2?family=Montserrat:wght@500;600&family=Oswald:wght@600&family=Ubuntu:wght@500&display=swap" rel="stylesheet">
<style>
  :root {
    --page: #ffffff;
    --navy-top: #121d2a;
    --navy-bottom: #080d15;
    --panel: #1c222c;
    --gold: #e9b23b;
    --gold-light: #f6d47c;
    --gold-deep: #b07a22;
    --bronze-line: #5a4128;
  }
  * { margin: 0; padding: 0; box-sizing: border-box; }
  html, body {
    width: 975px; height: 1200px; overflow: hidden;
    background: var(--page);
  }
  .canvas { position: relative; width: 975px; height: 1200px; }
  .invitation {
    position: absolute; left: 163px; top: 106px;
    width: 664px; height: 970px; overflow: hidden;
    background: linear-gradient(180deg, var(--navy-top) 0%, #0e1520 55%, var(--navy-bottom) 100%);
    font-family: "Montserrat", sans-serif;
    color: var(--gold);
    text-align: center;
  }
  .decor { position: absolute; inset: 0; }
  .text-line { position: absolute; left: 0; width: 100%; }
  .kicker { top: 58px; font-size: 15.5px; font-weight: 600; letter-spacing: 1px; }
  .event-name {
    top: 300px; font-family: "Montserrat", sans-serif; font-weight: 600;
    font-size: 34px; letter-spacing: 1px; color: var(--gold);
    display: flex; justify-content: center; align-items: center; gap: 10px;
  }
  .event-name .mark { width: 12px; height: 12px; border-radius: 50%; background: var(--gold); }
  .gala-title {
    top: 380px; font-family: "Ubuntu", sans-serif; font-weight: 500;
    font-size: 62px; line-height: 1; color: var(--gold);
  }
  .gala-subtitle { top: 456px; font-size: 20px; font-weight: 600; letter-spacing: 7px; padding-left: 8px; }
  .date-band {
    position: absolute; left: 171px; top: 694px; width: 321px; height: 27px;
    background: linear-gradient(90deg, var(--gold-deep), var(--gold) 40%, var(--gold-light) 60%, var(--gold-deep));
    clip-path: polygon(6% 0, 100% 0, 94% 100%, 0 100%);
    font-family: "Oswald", sans-serif; font-weight: 600; font-size: 19px;
    line-height: 27px; color: #1b1206; letter-spacing: 0.3px;
  }
  .date-band sup { font-size: 10px; }
  .time { top: 732px; font-size: 15px; font-weight: 500; }
  .menu { top: 768px; font-size: 19.5px; font-weight: 600; letter-spacing: 1px; }
  .venue { top: 802px; font-size: 19.5px; font-weight: 600; letter-spacing: 1px; line-height: 27px; }
  .details { top: 875px; font-size: 11.5px; font-weight: 500; line-height: 16px; }
  .ornament {
    position: absolute; left: 292px; width: 80px; height: 76px;
    background: radial-gradient(ellipse at 50% 60%, var(--gold-light), var(--gold-deep) 75%, transparent 76%);
  }
  .ornament-top { top: 158px; }
  .ornament-bottom { top: 546px; }
</style>
</head>
<body>
<div class="canvas">
  <main class="invitation">
    <svg class="decor" viewBox="0 0 664 970" width="664" height="970" aria-hidden="true">
      <defs>
        <linearGradient id="goldFoil" x1="0" y1="0" x2="1" y2="1">
          <stop offset="0" stop-color="#b07a22"/>
          <stop offset="0.45" stop-color="#f6d47c"/>
          <stop offset="0.7" stop-color="#e9b23b"/>
          <stop offset="1" stop-color="#a8721f"/>
        </linearGradient>
        <linearGradient id="panelFill" x1="0" y1="0" x2="0" y2="1">
          <stop offset="0" stop-color="#2a303a"/>
          <stop offset="1" stop-color="#0e1117"/>
        </linearGradient>
      </defs>
      <!-- background chevron lines -->
      <g class="chevron-lines" stroke="#5a4128" stroke-width="1" fill="none" opacity="0.8">
        <polyline points="0,343 332,12 664,342"/>
        <polyline points="0,590 332,922 664,590"/>
      </g>
      <!-- diagonal accent strokes -->
      <g class="accent-strokes" stroke="url(#goldFoil)" fill="none">
        <line x1="149" y1="98" x2="0" y2="256" stroke-width="2"/>
        <line x1="91" y1="200" x2="0" y2="296" stroke-width="2"/>
        <line x1="510" y1="639" x2="664" y2="478" stroke-width="2"/>
        <line x1="577" y1="604" x2="664" y2="511" stroke-width="2"/>
        <line x1="452" y1="112" x2="386" y2="178" stroke-width="10" opacity="0.75"/>
        <line x1="58" y1="596" x2="156" y2="498" stroke-width="18" opacity="0.6"/>
        <line x1="258" y1="656" x2="292" y2="622" stroke-width="7" opacity="0.6"/>
        <line x1="-4" y1="834" x2="86" y2="744" stroke-width="14" opacity="0.85"/>
      </g>
      <!-- central diamond frame -->
      <polygon class="frame-outer" points="332,114 609,391 332,668 55,391" fill="#151a22" stroke="#6b4c2c" stroke-width="1.5"/>
      <polygon class="frame-gold" points="332,138 585,391 332,644 79,391" fill="url(#panelFill)" stroke="url(#goldFoil)" stroke-width="5"/>
      <polygon class="frame-inner" points="332,152 571,391 332,630 93,391" fill="none" stroke="url(#goldFoil)" stroke-width="1.5"/>
    </svg>

    <div class="ornament ornament-top" role="img" aria-label="Gold art-deco lotus flourish at the top of the diamond frame"></div>
    <div class="ornament ornament-bottom" role="img" aria-label="Gold art-deco lotus flourish at the bottom of the diamond frame"></div>

    <p class="text-line kicker">JOIN US FOR A MEMORABLE NIGHT!</p>
    <p class="text-line event-name"><span class="mark"></span>Tovalmer</p>
    <h1 class="text-line gala-title">Gala</h1>
    <p class="text-line gala-subtitle">CELEBRATION</p>

    <p class="date-band">FRIDAY, NOVEMBER 8<sup>TH</sup></p>
    <p class="text-line time">6:30 – 10 P.M.</p>
    <p class="text-line menu">HORS D’OEUVRES AND COCKTAILS</p>
    <p class="text-line venue">THE MARLOWE<br>2460 NORTH CALDER STREET</p>
    <p class="text-line details">SEMI-FORMAL<br>TICKET INFORMATION ON REVERSE</p>
  </main>
</div>
</body>
</html>
```